Personal training studio poster / postcard

We need a poster / postcard design to advertise our recently established personal training studio - details and logo in the attached file. Logo file also provided.

We are flexible on format. Prefer the use of pictures in the design.

Training

```html
<!DOCTYPE html>
<html lang="en">
<head>
<meta charset="utf-8">
<title>Harbourside Strength Studio – Postcards</title>
<link href="https://fonts.googleapis.com/css2?family=Archivo:wght@500;700;800;900&display=swap" rel="stylesheet">
<style>
  :root {
    --backdrop: #b4b6b9;
    --card-border: #ffffff;
    --ink: #0b0b0b;
    --red: #e2232a;
    --red-deep: #9c1419;
    --silver-light: #f1f1f2;
    --silver: #bdbec0;
    --silver-dark: #8a8b8e;
    --grey-band: #3a3a3c;
    --white: #ffffff;
  }
  * { box-sizing: border-box; margin: 0; padding: 0; }
  html, body { width: 933px; height: 1200px; overflow: hidden; }
  body {
    background: var(--backdrop);
    font-family: "Archivo", Arial, sans-serif;
    position: relative;
  }
  .postcard {
    position: absolute;
    background: var(--card-border);
    padding: 18px;
    box-shadow: 4px 6px 14px rgba(0,0,0,.25);
  }
  .postcard__face {
    position: relative;
    width: 100%;
    height: 100%;
    background: var(--ink);
    overflow: hidden;
  }
  .postcard--services { left: 70px; top: 50px; width: 680px; height: 530px; }
  .postcard--schedule { left: 180px; top: 620px; width: 690px; height: 540px; }

  .studio-name {
    position: absolute;
    text-align: center;
    color: var(--silver);
    font-weight: 900;
    text-transform: uppercase;
    line-height: 1;
    letter-spacing: 1px;
  }
  .postcard--services .studio-name { left: 0; right: 0; top: 52px; font-size: 38px; }
  .postcard--schedule .studio-name { left: 200px; right: 10px; top: 70px; font-size: 46px; }
  .studio-name small { display: block; font-size: .62em; letter-spacing: 3px; margin-top: 6px; }

  .tagline-ribbon {
    position: absolute; left: 95px; top: 160px; width: 460px; height: 28px;
    background: linear-gradient(180deg, var(--silver-light), var(--silver) 60%, var(--silver-dark));
    color: var(--ink); font-weight: 800; font-size: 12.5px;
    display: flex; align-items: center; justify-content: center;
    text-transform: uppercase;
  }
  .booking {
    position: absolute; left: 300px; top: 198px; width: 340px;
    text-align: center; color: var(--white); font-weight: 500; font-size: 14px; line-height: 1.3;
  }
  .services-panel {
    position: absolute; left: 28px; top: 232px; width: 240px; height: 240px;
    background: linear-gradient(135deg, var(--red), var(--red-deep));
    color: var(--white); font-weight: 700; font-size: 16px; line-height: 1.25;
    padding: 16px 18px;
  }
  .services-panel ul { list-style: none; }
  .services-panel .sub { padding-left: 14px; }
  .services-panel .sub::before { content: "• "; }
  .services-panel .gap { margin-top: 12px; }

  .photo { position: absolute; }
  .photo--beach { left: 268px; top: 250px; width: 110px; height: 170px;
    background: linear-gradient(180deg, #8fb9d6, #4f8fb0 45%, #d9c9a8 70%, #c7b38d); }
  .photo--gym { left: 382px; top: 236px; width: 262px; height: 160px;
    background: linear-gradient(90deg, #2b2b2d, #9c8a7d 40%, #c7464a 75%, #2a2a2a); }

  .contact { position: absolute; left: 386px; top: 405px; color: var(--white); }
  .contact__phone { font-size: 17px; font-weight: 500; }
  .contact__address { margin-top: 4px; font-size: 12.5px; font-weight: 500; display: flex; align-items: center; gap: 5px; }

  .offer-band {
    position: absolute; left: 110px; top: 452px; width: 470px; height: 30px;
    background: linear-gradient(180deg, var(--silver-light), var(--silver) 60%, var(--silver-dark));
    color: var(--ink); font-weight: 900; font-size: 14.5px;
    display: flex; align-items: center; justify-content: center; text-transform: uppercase;
  }

  .photo--athlete { left: 0; top: 0; width: 270px; height: 100%;
    background: linear-gradient(180deg, #2a2a2a, #c99a80 22%, #b8866b 55%, #3b3b42 80%, #1b1b1f); }
  .grey-band { position: absolute; left: 520px; top: 280px; width: 140px; height: 110px; background: var(--grey-band); }
  .schedule-panel {
    position: absolute; left: 262px; top: 262px; width: 290px; height: 200px;
    background: linear-gradient(135deg, var(--red), var(--red-deep));
    color: var(--white); text-align: center; padding: 26px 10px;
    text-transform: none;
  }
  .class { margin-bottom: 14px; }
  .class__name { font-weight: 900; font-size: 19px; text-transform: uppercase; line-height: 1.05; }
  .class__time { font-weight: 800; font-size: 13px; }
  .class--inline .class__name { display: inline; }
</style>
</head>
<body>

<article class="postcard postcard--services">
  <div class="postcard__face">
    <div class="studio-name">Harbourside<small>Strength Studio</small></div>
    <div class="tagline-ribbon">Boutique personal and small group training studio</div>
    <div class="booking">Book online<br>www.harboursidestrength.com.au</div>

    <div class="services-panel">
      <ul>
        <li>Personal training</li>
        <li>Group fitness classes</li>
        <li class="sub">Yoga</li>
        <li class="sub">MMA conditioning</li>
        <li class="sub">Strength circuit</li>
        <li class="gap">Body composition coaching</li>
        <li>Nutrition advice</li>
        <li>Osteopathy</li>
      </ul>
    </div>

    <div class="photo photo--beach" role="img" aria-label="Woman meditating in a yoga pose on a beach"></div>
    <div class="photo photo--gym" role="img" aria-label="Women exercising on treadmills in the studio"></div>

    <div class="contact">
      <div class="contact__phone">Phone: 0412 555 018</div>
      <div class="contact__address">
        <svg width="10" height="14" viewBox="0 0 10 14" aria-hidden="true"><path d="M5 0a5 5 0 0 1 5 5c0 3.5-5 9-5 9S0 8.5 0 5a5 5 0 0 1 5-5z" fill="#e2232a"/><circle cx="5" cy="5" r="2" fill="#fff"/></svg>
        4/18 Meridian Road Harbourside
      </div>
    </div>

    <div class="offer-band">August special – all group fitness classes $10</div>
  </div>
</article>

<article class="postcard postcard--schedule">
  <div class="postcard__face">
    <div class="photo photo--athlete" role="img" aria-label="Fit woman in sports top holding a dumbbell"></div>
    <div class="studio-name">Harbourside<small>Strength Studio</small></div>
    <div class="grey-band"></div>
    <div class="schedule-panel">
      <div class="class"><div class="class__name">Strength circuit</div><div class="class__time">Tuesdays 6:15am</div></div>
      <div class="class"><div class="class__name">MMA conditioning</div><div class="class__time">Tuesdays and Thursdays 6:15pm</div></div>
      <div class="class class--inline"><div class="class__name">Yoga</div> <span class="class__time">– Saturdays 9am</span></div>
    </div>
  </div>
</article>

</body>
</html>
```